Premium Fitness Meal Plan Design for VoltaKor (Brand Like PlumQuarry!)

VoltaKor 6 Week Autumn Forge Meal Plan Design (Branded Handout)

πŸ“„ Overview:
We are looking for a professionally designed, branded meal plan handout for our fitness facility, VoltaKor. This meal plan will be used during our upcoming 6 Week Autumn Forge Quest, where members aim to lose body fat, build lean muscle, and improve their energy through nutrition and strength training.

The design should be highly polished, visually engaging, and reflect our brand quality β€” something on par with what you would see from larger national gym chains (e.g., Plum Quarry, K62, Delmar’s Drillyard). This is not just a text document β€” we want it to feel premium, motivating, and easy to follow, ideally something members are excited to reference and share.

🧾 Format & Layout:
Size: Standard 8.5x11 inch format (single or double-sided)

Final Output: Print-ready PDF + editable source files

Orientation: Portrait

Can be designed as either:

One visually organized front-and-back sheet

Or two clean, digestible pages presented as a mini-handout

🎨 Design Style:
Clean, energetic, and transformation-focused

Use brand colors and fonts that feel bold, fresh, and motivating

Include icons, dividers, or visual cues to separate sections (not just blocks of text)

Sections should feel approachable and empowering, not clinical or restrictive

Include room for the VoltaKor logo (provided) at the top and/or footer

πŸ“˜ Content to Include:
The following content should be visually structured and formatted in clear, engaging blocks. We’ll provide this content in a PDF format

1. Header Title:
"VoltaKor 6 Week Autumn Forge Nutrition Blueprint"

2. Introduction (Small Block):
Short blurb about the challenge goals (lose body fat, gain energy, preserve lean muscle mass)

3. Elimination List (Foods to Avoid):
A visually separated section with a list of foods and drinks that should be eliminated or greatly reduced for fat loss

4. Smart Swaps Table:
A side-by-side "Craving vs Swap" table that shows easy alternatives to popular bad habits (e.g., soda β†’ sparkling water)

5. Build-Your-Own Meal Plan Sections:
Organize these into clear categories:

Proteins

Carbs

Fats

Veggies

Extras / Smart Swaps
Use icons, color codes, or visual grids to organize these food lists

6. Tips Section (Optional Bonuses):
Hydration goal

Suggested number of meals

Protein shake recommendation

Meal timing tip

10-min walk after dinner tip

πŸ“¦ Files Provided:

All written content in organized text format

βœ… Deliverables:
Final design in print-ready PDF

Editable source file (AI, PSD, or InDesign preferred)

πŸ™Œ Inspiration:
Design should feel in line with the type of professional print materials used by high-end fitness studios. Clean lines, engaging fonts, and premium layout. We're not looking for clipart or gimmicky stock photos β€” we want the design to reflect the premium, results-driven experience our gym provides.

```html
<!DOCTYPE html>
<html lang="en">
<head>
<meta charset="utf-8">
<title>VoltaKor – Nutrition Handout, Side 2</title>
<link rel="stylesheet" href="https://fonts.googleapis.com/css2?family=Outfit:wght@800&family=Nunito:wght@400;600;800&display=swap">
<style>
  :root {
    --page-bg: #ececec;
    --label: #333333;
    --panel: #2b2b2b;
    --text: #ffffff;
    --rule: #d9d9d9;
    --brand-yellow: #f3d41a;
    --stop-red: #d8401e;
    --swap-green: #93c01f;
    --photo-yellow: #e9c60d;
    --photo-amber: #d49a12;
    --photo-wood: #a4551f;
  }
  * { box-sizing: border-box; margin: 0; padding: 0; }
  html, body { width: 1200px; height: 1200px; overflow: hidden; }
  body {
    position: relative;
    background: var(--page-bg);
    font-family: "Nunito", sans-serif;
    color: var(--text);
  }
  .sheet-label, .fold-label {
    position: absolute;
    color: var(--label);
    font-family: "Nunito", sans-serif;
    transform: translateX(-50%);
    line-height: 1;
  }
  .sheet-label { left: 600px; top: 170px; font-size: 31px; }
  .fold-label { top: 212px; font-size: 21px; }

  .spread {
    position: absolute;
    left: 92px; top: 242px;
    width: 1015px; height: 784px;
  }
  .photo-backdrop {
    position: absolute; inset: 0;
    background:
      radial-gradient(ellipse 260px 340px at 830px 500px, var(--photo-wood) 0%, rgba(164,85,31,0.6) 55%, transparent 100%),
      linear-gradient(135deg, var(--photo-yellow) 0%, var(--photo-amber) 60%, var(--photo-yellow) 100%);
  }
  .content-panel {
    position: absolute;
    left: 36px; top: 29px;
    width: 609px; height: 721px;
    background: var(--panel);
  }
  .logo-box {
    position: absolute;
    left: 645px; top: 29px;
    width: 250px; height: 89px;
    background: var(--panel);
    display: flex; align-items: center; justify-content: center;
  }
  .logo-name {
    font-family: "Nunito", sans-serif;
    font-weight: 800;
    font-size: 38px;
    color: var(--brand-yellow);
  }

  .section-icon { position: absolute; left: 21px; width: 93px; height: 93px; }
  .section-title {
    position: absolute; left: 134px;
    font-family: "Outfit", sans-serif;
    font-weight: 800;
    font-size: 21px;
    line-height: 25px;
    text-transform: uppercase;
    white-space: nowrap;
  }
  .section-intro {
    position: absolute; left: 134px;
    font-size: 15.3px; line-height: 18px;
    white-space: nowrap;
  }

  .eliminate-icon { top: 21px; }
  .eliminate-title { top: 22px; }
  .eliminate-intro { top: 73px; }

  .eliminate-list {
    position: absolute; top: 127px;
    list-style: none;
    font-size: 12.8px; line-height: 15.2px;
    white-space: nowrap;
  }
  .eliminate-list li { position: relative; padding-left: 13px; margin-bottom: 2.6px; }
  .eliminate-list li::before { content: "•"; position: absolute; left: 0; }
  .eliminate-list.col-a { left: 24px; }
  .eliminate-list.col-b { left: 295px; }

  .section-rule {
    position: absolute; left: 22px; top: 319px;
    width: 547px; height: 1px; background: var(--rule);
  }

  .swap-icon { top: 338px; }
  .swap-title { top: 341px; }
  .swap-intro { top: 367px; }

  .swap-table {
    position: absolute; left: 22px; top: 444px;
    border-collapse: collapse;
    font-size: 12.4px;
  }
  .swap-table th { font-weight: 800; text-align: left; height: 22.4px; }
  .swap-table td { height: 22.4px; white-space: nowrap; }
  .swap-table .craving { width: 130px; }
</style>
</head>
<body>
  <div class="sheet-label">Side 2</div>
  <div class="fold-label" style="left:261px">2</div>
  <div class="fold-label" style="left:600px">3</div>
  <div class="fold-label" style="left:937px">4</div>

  <section class="spread">
    <div class="photo-backdrop" role="img" aria-label="Photo of sliced oranges and watermelon on a wooden cutting board over a yellow wood table with a tropical leaf"></div>

    <div class="logo-box"><span class="logo-name">VoltaKor</span></div>

    <div class="content-panel">
      <svg class="section-icon eliminate-icon" viewBox="0 0 92 92" role="img" aria-label="Crossed-out junk food and drinks icon">
        <circle cx="46" cy="46" r="42" fill="none" stroke="var(--stop-red)" stroke-width="6"/>
        <line x1="17" y1="17" x2="75" y2="75" stroke="var(--stop-red)" stroke-width="6"/>
      </svg>
      <h2 class="section-title eliminate-title">Foods &amp; Drinks to Eliminate<br>(or Greatly Reduce)</h2>
      <p class="section-intro eliminate-intro">These are the biggest culprits sabotaging fat loss highly<br>palatable, calorie-dense, and metabolically disruptive:</p>

      <ul class="eliminate-list col-a">
        <li>Sugary drinks (sodas, energy drinks,<br>sweet teas, juice blends)</li>
        <li>Fancy coffee drinks (Frostaccinos,<br>sugary creamers, flavor pumps)</li>
        <li>Fast food and fried foods (even<br>“grilled” items often packed with oils)</li>
        <li>Packaged snacks (chips, cookies,<br>granola bars, trail mix with candy)</li>
        <li>Baked goods (donuts, muffins, pastries,<br>bagels with cream cheese)</li>
      </ul>
      <ul class="eliminate-list col-b">
        <li>Alcohol (especially beer and sugary<br>mixers)</li>
        <li>Processed carbs (white breads, crackers,<br>pasta)</li>
        <li>Cheese-heavy meals (pizza, nachos,<br>quesadillas)</li>
        <li>High-fat deli meats (salami, pepperoni,<br>sausage)</li>
        <li>Sauces and condiments loaded with sugar<br>(ketchup, BBQ sauce, honey mustard)</li>
      </ul>

      <div class="section-rule"></div>

      <svg class="section-icon swap-icon" viewBox="0 0 92 92" role="img" aria-label="Healthy food icon with water bottle, broccoli, salad and chicken">
        <circle cx="46" cy="46" r="42" fill="none" stroke="var(--swap-green)" stroke-width="6"/>
      </svg>
      <h2 class="section-title swap-title">Smart Swaps for Fat Loss</h2>
      <p class="section-intro swap-intro">Instead of cutting everything and feeling deprived,<br>make these easy grocery-store swaps that still satisfy<br>cravings without killing your progress:</p>

      <table class="swap-table">
        <thead>
          <tr><th class="craving">Craving</th><th>Try This Instead</th></tr>
        </thead>
        <tbody>
          <tr><td>Soda</td><td>Sparkling water with lime, Fizzleaf, or plain water with fruit infusions</td></tr>
          <tr><td>Fancy Coffee</td><td>Coffee with unsweetened almond milk + stevia drops or cinnamon</td></tr>
          <tr><td>Chips</td><td>Rice cakes, roasted chickpeas, or crunchy cucumber with Chilimo</td></tr>
          <tr><td>Ice Cream</td><td>Frozen banana blended with protein powder (DIY "nice cream")</td></tr>
          <tr><td>Candy</td><td>Berries, apples or dark chocolate squares (85%+)</td></tr>
          <tr><td>Pasta</td><td>Zucchini noodles, chickpea pasta, or cauliflower rice</td></tr>
          <tr><td>Pizza</td><td>Egg white wraps or low-carb tortillas with turkey pepperoni and light cheese</td></tr>
          <tr><td>Alcohol</td><td>Limit to 1x/week if needed</td></tr>
          <tr><td>Sandwich Bread</td><td>Sprouthaus bread, low-carb wraps, or lettuce wraps</td></tr>
          <tr><td>Heavy Sauces</td><td>Mustard, salsa, hot sauce, coconut aminos, Greek yogurt-based dips</td></tr>
        </tbody>
      </table>
    </div>
  </section>
</body>
</html>
```